Velvet comb home studio

VELVET COMB.....at fox valley ,Wahroonga is a home hairdressing studio.
Hair services from a peaceful setting.
Quality colours and products.
free consultation prior to making appointment.
Easy and convenient after hours hair appointments.
Qualified hairdresser with over 15 years experience.
Specialise in foiling,balayage,ombre colour,tints,style cutting and blowdrying.
20 % off for new clients(colour services)
sms or call for 0491302667 for a quote.
Updates
im sorry guys but i has to re do alot of the photos. i would like something that looks elegant and classy.i will post an example of a flier style i like Added Wednesday, April 27, 2016
Project Deadline Extended Reason: im sorry i have decided i needed better photographs. please design again...i will choose someone before the deadline. please an elegant design will be great Added Wednesday, April 27, 2016
Target Market(s)
18-60 year olds
Industry/Entity Type
Hair
Requirements
Must have
- Must say home hairdressing studio
- Must say Velvet Comb at Fox Valley Wahroonga
- Must say phone number
Nice to have
- Modern but still classy and elegant
- Try to incorporate any photos which I have uploaded that looks best

```html
<!DOCTYPE html>
<html lang="en">
<head>
<meta charset="utf-8">
<title>Velvet Comb – home hairdressing studio flyer</title>
<link rel="stylesheet" href="https://fonts.googleapis.com/css2?family=Jost:ital,wght@0,500;0,600;1,400;1,500;1,600&family=Playfair+Display:ital,wght@1,900&display=swap">
<style>
  :root {
    --page-bg: #c9c9cb;
    --card-black: #050505;
    --ink-white: #ffffff;
    --ink-soft: #e6e6e6;
    --silver-light: #f2f2f2;
    --silver-mid: #9d9d9d;
    --silver-dark: #4a4a4a;
    --badge-red: #d62027;
  }
  * { margin: 0; padding: 0; box-sizing: border-box; }
  html, body { width: 1200px; height: 1200px; overflow: hidden; }
  body {
    background: radial-gradient(circle at 50% 40%, #e4e4e6 0%, var(--page-bg) 75%);
    font-family: "Jost", "Futura", sans-serif;
    position: relative;
  }
  .flyer {
    position: absolute;
    left: 50px; top: 210px;
    width: 1100px; height: 780px;
    background: var(--card-black);
    color: var(--ink-white);
    overflow: hidden;
    box-shadow: 0 10px 30px rgba(0,0,0,.25);
  }
  .masthead { position: absolute; left: 0; top: 0; width: 100%; height: 165px; }
  .brand { position: absolute; left: 42px; top: 46px; }
  .brand-lockup { display: flex; align-items: center; gap: 16px; }
  .brand-dot { width: 30px; height: 30px; border-radius: 50%; background: var(--ink-white); }
  .brand-name {
    font-family: "Jost", sans-serif; font-weight: 600; font-size: 38px;
    letter-spacing: 2px; line-height: 1;
  }
  .brand-location {
    margin: 10px 0 0 47px;
    font-style: italic; font-weight: 400; font-size: 19px;
    color: var(--ink-soft); letter-spacing: .5px; line-height: 1;
  }
  .tagline {
    position: absolute; left: 493px; top: 64px;
    font-family: "Playfair Display", serif; font-style: italic; font-weight: 900;
    font-size: 46px; letter-spacing: -0.5px; line-height: 1;
    white-space: nowrap;
  }
  .silver-band {
    position: absolute; left: 0; width: 100%; height: 14px;
    background: linear-gradient(180deg, var(--silver-dark) 0%, var(--silver-light) 45%, var(--silver-mid) 100%);
  }
  .silver-band.top { top: 165px; }
  .silver-band.bottom { top: 531px; }
  .gallery { position: absolute; left: 0; top: 206px; width: 100%; height: 300px; }
  .gallery-photo { position: absolute; top: 0; height: 300px; }
  .photo-blonde { left: 0; width: 350px; background: linear-gradient(110deg, #f4ead8 0%, #e9dccb 45%, #d8cfc6 100%); }
  .photo-bronze { left: 375px; width: 344px; background: linear-gradient(120deg, #6b4424 0%, #b88654 45%, #5a3a22 100%); }
  .photo-brunette { left: 744px; width: 356px; background: linear-gradient(100deg, #8a6a50 0%, #e8ddd4 50%, #f4f2f0 100%); }
  .gallery-divider {
    position: absolute; top: 0; width: 25px; height: 300px;
    background: linear-gradient(90deg, var(--silver-dark) 0%, var(--silver-light) 50%, var(--silver-dark) 100%);
  }
  .divider-one { left: 350px; }
  .divider-two { left: 719px; }
  .features {
    position: absolute; top: 567px; font-style: italic; font-weight: 400;
    font-size: 24.5px; line-height: 28.5px; list-style: none;
  }
  .features.left { left: 32px; width: 545px; white-space: nowrap; }
  .features.right { left: 578px; width: 490px; }
  .features li::before { content: "•"; font-style: normal; margin-right: 8px; }
  .offer {
    position: absolute; left: 43px; top: 696px;
    display: flex; align-items: center; gap: 10px;
  }
  .offer-badge {
    width: 56px; height: 56px; border-radius: 50%; background: var(--badge-red);
    display: flex; flex-direction: column; align-items: center; justify-content: center;
    font-weight: 600; font-size: 19px; line-height: 17px;
  }
  .offer-text { font-style: italic; font-weight: 500; font-size: 18px; text-transform: uppercase; }
  .call-to-action {
    position: absolute; right: 33px; top: 709px;
    font-style: italic; font-weight: 500; font-size: 24.5px; text-transform: uppercase;
    white-space: nowrap;
  }
</style>
</head>
<body>
  <article class="flyer">
    <header class="masthead">
      <div class="brand">
        <div class="brand-lockup">
          <span class="brand-dot"></span>
          <span class="brand-name">VELVET COMB</span>
        </div>
        <p class="brand-location">at Fox Valley, Wahroonga</p>
      </div>
      <h1 class="tagline">home hairdressing studio</h1>
    </header>

    <div class="silver-band top"></div>

    <section class="gallery">
      <div class="gallery-photo photo-blonde" role="img" aria-label="Photo of a woman with long wavy platinum blonde hair"></div>
      <div class="gallery-divider divider-one"></div>
      <div class="gallery-photo photo-bronze" role="img" aria-label="Photo of a woman with voluminous bronze-brown curls"></div>
      <div class="gallery-divider divider-two"></div>
      <div class="gallery-photo photo-brunette" role="img" aria-label="Photo of a woman with tousled brunette waves"></div>
    </section>

    <div class="silver-band bottom"></div>

    <ul class="features left">
      <li>Hair services from a peaceful setting.</li>
      <li>Quality colours and products.</li>
      <li>free consultation prior to making appointment.</li>
      <li>Easy and convenient after hours hair appmnts.</li>
    </ul>
    <ul class="features right">
      <li>Qualified hairdresser with over 15 years experience.</li>
      <li>Specialise in foiling,balayage,ombre colour, tints, style cutting and blowdrying.</li>
    </ul>

    <div class="offer">
      <div class="offer-badge"><span>20%</span><span>OFF</span></div>
      <span class="offer-text">For new clients(colour services)</span>
    </div>
    <p class="call-to-action">SMS or call for 0491302667 for a quote.</p>
  </article>
</body>
</html>
```